Borchures
Need help selling me and my services
potential customers at local companies to provide them with welding support and produce parts to take the load off their hands
just have to do your best to help sell myself as a young man & business! I have the skills to do the jobs. Just need the help with the big words to convince others that their in good hands

```html
<!DOCTYPE html>
<html lang="en">
<head>
<meta charset="utf-8">
<title>Vornep Enterprises LLC – Welding Brochure</title>
<link href="https://fonts.googleapis.com/css2?family=Open+Sans:wght@400;600;700;800&display=swap" rel="stylesheet">
<style>
  :root{
    --navy:#0a1633;
    --navy-deep:#060d22;
    --blue:#1666b8;
    --blue-bright:#2f9be6;
    --sky:#7cc8f5;
    --ice:#dff1fc;
    --white:#ffffff;
    --ink:#1c2a44;
    --label:#8a8f99;
  }
  *{margin:0;padding:0;box-sizing:border-box;}
  html,body{width:1200px;height:403px;overflow:hidden;background:var(--white);}
  body{font-family:"Open Sans",Arial,sans-serif;position:relative;color:var(--white);}

  .spread{position:absolute;top:16px;width:590px;height:380px;display:flex;box-shadow:0 1px 4px rgba(0,0,0,.25);}
  .spread--outside{left:4px;}
  .spread--inside{left:606px;}
  .page-label{position:absolute;top:-12px;width:295px;font-size:6px;color:var(--label);text-align:center;}
  .page-label--a{left:0;}
  .page-label--b{left:295px;}
  .panel{position:relative;width:295px;height:380px;overflow:hidden;}

  .swoosh{position:absolute;inset:0;width:100%;height:100%;}
  .photo{position:absolute;}

  /* back cover */
  .panel--back{background:var(--white);}
  .panel--back .photo--artwork{left:0;top:0;width:295px;height:230px;
    background:linear-gradient(160deg,#1b3e70 0%,#3b86c6 45%,#cfe9fb 100%);}
  .contact{position:absolute;left:150px;top:262px;width:135px;color:var(--ink);font-size:5.6px;line-height:1.55;text-align:right;}
  .contact h3{font-size:6.4px;font-weight:700;color:var(--blue);margin-top:6px;}

  /* front cover */
  .panel--front{background:var(--navy);}
  .cover-title{position:absolute;left:0;top:14px;width:295px;height:22px;background:linear-gradient(90deg,var(--blue),var(--blue-bright));
    font-size:12px;font-weight:800;text-align:center;line-height:22px;letter-spacing:.2px;}
  .panel--front .photo--welder{left:12px;top:44px;width:271px;height:210px;border-radius:4px;
    background:radial-gradient(circle at 35% 68%,#ffffff 0%,#bfe6ff 6%,#3d8fd0 22%,#1b3e70 48%,#0b1836 80%);}
  .brand{position:absolute;left:0;top:296px;width:295px;text-align:center;}
  .brand__dot{display:inline-block;width:20px;height:20px;border-radius:50%;background:var(--blue);vertical-align:middle;margin-right:6px;}
  .brand__name{display:inline-block;vertical-align:middle;font-size:17px;font-weight:800;color:var(--navy);letter-spacing:1px;}
  .brand__sub{font-size:6px;font-weight:800;color:var(--navy);letter-spacing:1px;margin-top:1px;}
  .brand__tag{font-size:4.5px;color:var(--blue);margin-top:1px;}

  /* inside left */
  .panel--inside-left{background:var(--navy);}
  .panel--inside-left .photo--sparks{left:0;top:0;width:295px;height:200px;
    background:radial-gradient(circle at 40% 45%,#bfe6ff 0%,#4d9ad6 18%,#1b3e70 50%,#0a1633 85%);}
  .panel--inside-left .photo--worker{left:0;top:212px;width:295px;height:168px;
    background:linear-gradient(160deg,#27486f 0%,#5d7d9c 40%,#a7b9c8 65%,#3a5674 100%);}

  /* inside right */
  .panel--inside-right{background:linear-gradient(180deg,var(--navy) 0%,var(--navy-deep) 100%);}
  .inside-brand{position:absolute;right:14px;top:8px;text-align:right;}
  .inside-brand .brand__dot{width:12px;height:12px;margin-right:4px;}
  .inside-brand .brand__name{font-size:11px;color:var(--white);}
  .inside-brand .brand__sub{font-size:4.5px;color:var(--sky);}
  .section-head{position:absolute;left:12px;font-size:6.4px;font-weight:700;color:var(--white);
    background:var(--blue);padding:1px 6px;border-radius:2px;}
  .copy{position:absolute;left:12px;width:272px;font-size:5.2px;line-height:1.5;color:var(--ice);}
  .services{position:absolute;left:12px;top:196px;width:150px;list-style:none;}
  .services li{display:flex;align-items:center;height:15px;font-size:5.6px;font-weight:600;color:var(--white);}
  .services svg{width:7px;height:7px;margin-right:5px;flex:none;}
  .photo--thumbs{right:12px;width:110px;height:40px;border-radius:3px;
    background:linear-gradient(135deg,#1e4f8c,#6fb6e6 55%,#153460);}
  .photo--thumb-a{top:196px;}
  .photo--thumb-b{top:242px;}
  .photo--strip{left:0;top:300px;width:295px;height:80px;
    background:linear-gradient(120deg,#0e2a52 0%,#2c6eb0 45%,#cfe9fb 58%,#2a5f99 72%,#0a1a38 100%);}
</style>
</head>
<body>

<section class="spread spread--outside">
  <span class="page-label page-label--a">Page 4</span>
  <span class="page-label page-label--b">Page 1</span>

  <article class="panel panel--back">
    <div class="photo photo--artwork" role="img" aria-label="Welding torch artwork in blue tones"></div>
    <svg class="swoosh" viewBox="0 0 295 380" preserveAspectRatio="none" aria-hidden="true">
      <path d="M0 340 C90 330 200 355 295 320 L295 380 L0 380 Z" fill="#dff1fc"/>
      <path d="M0 360 C100 345 200 372 295 345 L295 380 L0 380 Z" fill="#1666b8"/>
    </svg>
    <div class="contact">
      <h3>Contact Details</h3>
      <p>Vornep Enterprises LLC</p>
      <p>1748 Ridgeline Ave, Suite 4</p>
      <p>Dayton, OH 45402</p>
      <h3>Owner Info</h3>
      <p>Marcus Vell, Owner</p>
      <p>Phone: (555) 014-2280</p>
      <p>E-mail: info@pelaworks.com</p>
    </div>
  </article>

  <article class="panel panel--front">
    <h1 class="cover-title">PROMOTE MY WELDING COMPANY</h1>
    <div class="photo photo--welder" role="img" aria-label="Welder at work with bright sparks"></div>
    <svg class="swoosh" viewBox="0 0 295 380" preserveAspectRatio="none" aria-hidden="true">
      <path d="M0 268 C90 240 200 290 295 250 L295 380 L0 380 Z" fill="#2f9be6"/>
      <path d="M0 280 C100 258 200 300 295 266 L295 380 L0 380 Z" fill="#ffffff"/>
      <path d="M0 360 C100 345 200 372 295 345 L295 380 L0 380 Z" fill="#1666b8"/>
    </svg>
    <div class="brand">
      <span class="brand__dot"></span><span class="brand__name">VORNEP</span>
      <div class="brand__sub">ENTERPRISES LLC</div>
      <div class="brand__tag">WELDING SUPPORT &amp; PARTS PRODUCTION</div>
    </div>
  </article>
</section>

<section class="spread spread--inside">
  <span class="page-label page-label--a">Page 2</span>
  <span class="page-label page-label--b">Page 3</span>

  <article class="panel panel--inside-left">
    <div class="photo photo--sparks" role="img" aria-label="Welding arc throwing sparks"></div>
    <div class="photo photo--worker" role="img" aria-label="Young welder working at a bench"></div>
    <svg class="swoosh" viewBox="0 0 295 380" preserveAspectRatio="none" aria-hidden="true">
      <path d="M0 200 C90 170 200 230 295 180 L295 214 C200 250 100 200 0 226 Z" fill="#0a1633"/>
      <path d="M0 198 C90 168 200 226 295 178 L295 186 C200 234 90 180 0 208 Z" fill="#2f9be6"/>
    </svg>
  </article>

  <article class="panel panel--inside-right">
    <div class="inside-brand">
      <span class="brand__dot"></span><span class="brand__name">VORNEP</span>
      <div class="brand__sub">ENTERPRISES LLC</div>
    </div>
    <h2 class="section-head" style="top:42px;">Mission Statement</h2>
    <p class="copy" style="top:56px;">We provide local companies with dependable welding support and precision parts production, so your team can stay focused on its core work. Every job is done on time, to spec and with pride.</p>
    <p class="copy" style="top:84px;">Young, driven and fully skilled, we take the load off your hands with clean welds, honest pricing and quick turnaround. When you hand us a project, you can trust it is in good hands from start to finish.</p>
    <h2 class="section-head" style="top:146px;">Skilled Welder Support</h2>
    <p class="copy" style="top:160px;">Short runs or steady contracts, we adapt to your schedule and deliver quality you can build on.</p>
    <ul class="services">
      <li><svg viewBox="0 0 8 8"><path d="M1 4 L3 6 L7 1.5" stroke="#7cc8f5" stroke-width="1.4" fill="none"/></svg>Custom Fabrication</li>
      <li><svg viewBox="0 0 8 8"><path d="M1 4 L3 6 L7 1.5" stroke="#7cc8f5" stroke-width="1.4" fill="none"/></svg>Structural Welding</li>
      <li><svg viewBox="0 0 8 8"><path d="M1 4 L3 6 L7 1.5" stroke="#7cc8f5" stroke-width="1.4" fill="none"/></svg>Repair Work</li>
      <li><svg viewBox="0 0 8 8"><path d="M1 4 L3 6 L7 1.5" stroke="#7cc8f5" stroke-width="1.4" fill="none"/></svg>Parts Production and Machining</li>
      <li><svg viewBox="0 0 8 8"><path d="M1 4 L3 6 L7 1.5" stroke="#7cc8f5" stroke-width="1.4" fill="none"/></svg>On-Site Service</li>
      <li><svg viewBox="0 0 8 8"><path d="M1 4 L3 6 L7 1.5" stroke="#7cc8f5" stroke-width="1.4" fill="none"/></svg>Quick Turnaround</li>
    </ul>
    <div class="photo photo--thumbs photo--thumb-a" role="img" aria-label="Welded steel parts"></div>
    <div class="photo photo--thumbs photo--thumb-b" role="img" aria-label="Fabricated metal frame"></div>
    <div class="photo photo--strip" role="img" aria-label="Welder in protective mask working with sparks"></div>
    <svg class="swoosh" viewBox="0 0 295 380" preserveAspectRatio="none" aria-hidden="true">
      <path d="M0 300 C100 284 200 316 295 292 L295 300 C200 322 100 292 0 306 Z" fill="#2f9be6"/>
    </svg>
  </article>
</section>

</body>
</html>
```